Wellness, Purpose, and the Quiet Path Research Program Website

Overview: This website will serve a new research program (Wellness, Purpose, and the Quiet Path) at the Thornbury University School of Medicine. I want a clean, intuitive design that has a navigation bar, but uses icons/graphic buttons to link to the main pages. In an attached Word document, I have provided a basic information architecture for the site, understanding that this project would just generate graphics and code for the 3 pages. I highlighted the 3 pages I'd like designed.
Target market: People who want to participate in our research, or contribute grant funding to specific projects.
Number of page: The design project focuses on 3 pages, but the site must accommodate 6 pages with top-level links. See attached Word doc.
Logo and website header: Please integrate our logo in the header. I've uploaded it as a png file--both with the name of the website and with just the logo image. I imaging the logo would look great in a banner set against an image of a mountain. The two main design themes I want to see included are nature and healthcare.
Text content: I have not yet provided text. Use some dummy text.
Technical Specifications:
- Build using WordPress. We will host this site ourselves on HostBarrow using WordPress.
- The design package must be coded.
- The template must be responsive to different platforms (e.g., computer, mobile phone, Zelvo).
Thank you! I look forward to seeing your designs.
- Ned

```html
<!DOCTYPE html>
<html lang="en">
<head>
<meta charset="utf-8">
<title>Wellness, Purpose, and the Quiet Path Research Program</title>
<link href="https://fonts.googleapis.com/css2?family=Arimo:wght@400;700&display=swap" rel="stylesheet">
<style>
:root{
  --blue:#1a5a97;
  --blue-dark:#134a80;
  --green:#7cb342;
  --green-deep:#23895a;
  --ink:#222;
  --muted:#444;
  --card:#f7f7f7;
  --line:#bdbdbd;
}
*{box-sizing:border-box;margin:0;padding:0}
html,body{width:1200px;height:4562px;overflow:hidden}
body{position:relative;font-family:"Arimo",Arial,sans-serif;color:var(--ink);background:#fff}
.abs{position:absolute}
.photo{position:absolute}

/* header */
.hero{left:0;top:0;width:1200px;height:690px;background:linear-gradient(180deg,#cfe4ee 0%,#9fbfcf 30%,#5f7f62 55%,#7a9aa6 75%,#4d6570 100%)}
.brand{position:absolute;display:flex;align-items:center;gap:10px;font-weight:700;color:var(--blue)}
.brand .dot{width:22px;height:22px;border-radius:50%;background:var(--green)}
.hero .brand{left:62px;top:58px;width:200px;font-size:16px;line-height:1.25}
.nav{position:absolute;top:68px;left:420px;display:flex;gap:37px;font-size:17px;color:#111}
.nav a{color:inherit;text-decoration:none}
.nav a.active{color:var(--blue);font-weight:700}
.hero-title{position:absolute;left:269px;top:308px;width:660px;height:58px;background:var(--green-deep);color:#fff;font-weight:700;font-size:42px;line-height:58px;padding-left:14px}
.hero-sub{position:absolute;left:283px;top:372px;width:531px;height:127px;background:var(--green);color:#fff;font-size:28px;line-height:41px;padding:3px 0 0 17px;border-left:4px solid var(--green-deep)}

.tag-brand{left:398px;top:724px;font-size:13px;line-height:1.3;gap:12px}
.tag-brand small{display:block;color:var(--green);font-size:11px}

.h-main{color:var(--blue);font-weight:700}
.intro-title{left:0;width:1200px;top:812px;text-align:center;font-size:48px}
.intro-text{left:150px;width:900px;top:900px;text-align:center;font-size:22px;line-height:42px;color:var(--muted)}

/* feature cards */
.card{position:absolute;top:1067px;width:294px;height:349px;background:var(--card);box-shadow:0 1px 5px rgba(0,0,0,.25);text-align:center}
.card .icon{position:absolute;left:20px;top:-26px;width:96px;height:96px;background:#fff;box-shadow:0 1px 5px rgba(0,0,0,.2);display:flex;align-items:center;justify-content:center}
.card .label{position:absolute;left:130px;top:52px;color:var(--green-deep);font-weight:700;font-size:20px;text-decoration:underline}
.card p{position:absolute;left:22px;right:22px;top:100px;font-size:16px;line-height:29px;color:var(--muted)}
.btn{position:absolute;display:flex;align-items:center;justify-content:center;border-radius:30px;text-decoration:none}
.btn-outline{border:2px solid var(--green);color:#333;background:transparent}
.btn-solid{background:var(--green);color:#fff}
.card .btn{left:89px;top:300px;width:116px;height:34px;font-size:13px}

/* doctor */
.doc-photo{left:28px;top:1504px;width:572px;height:381px;background:linear-gradient(135deg,#e8ecef,#c9ced2 60%,#8b7a6a)}
.about-title{left:658px;top:1520px;font-size:38px}
.about-text{left:656px;top:1600px;width:460px;font-size:23px;line-height:42px;color:var(--muted)}
.about-btn{left:775px;top:1809px;width:193px;height:58px;font-size:22px}

/* spiritual */
.spirit{left:0;top:1924px;width:1200px;height:596px;background:linear-gradient(180deg,#cdd9e0 0%,#b9c8d1 55%,#cbbda9 100%)}
.spirit-title{left:106px;top:2005px;font-size:40px}
.spirit-text{left:108px;top:2096px;width:640px;font-size:23px;line-height:42px;color:#333}
.spirit-btn{left:122px;top:2411px;width:195px;height:60px;font-size:22px}

/* people */
.people-title{left:106px;top:2562px;font-size:40px}
.people-text{left:108px;top:2620px;width:1000px;font-size:23px;line-height:42px;color:#333}
.people-btn{left:926px;top:2689px;width:178px;height:55px;font-size:21px}
.team{position:absolute;top:2784px;width:361px}
.team .head{height:54px;background:var(--blue);color:#fff;font-size:28px;line-height:54px;padding-left:24px;border-radius:10px 10px 0 0}
.team .pic{height:233px}
.team p{text-align:center;font-size:23px;line-height:36px;color:#333;margin-top:28px;padding:0 12px}
.team .btn{position:relative;margin:34px auto 0;width:135px;height:40px;font-size:15px}

/* project */
.project{left:0;top:3390px;width:1200px;height:513px;background:linear-gradient(135deg,#2a6db0,#1b5b98 60%,#3f7fbc)}
.project-title{left:103px;top:3466px;font-size:40px;color:#fff;font-weight:700}
.project-text{left:108px;top:3548px;width:1000px;font-size:23px;line-height:42px;color:#fff}
.project-btn{left:934px;top:3805px;width:162px;height:43px;font-size:21px;border:2px solid #fff;border-radius:8px;color:#fff}

/* faq */
.faq{left:0;top:3903px;width:1200px;height:531px;background:linear-gradient(135deg,#e4e4e4,#cfcfcf 60%,#e2e2e2)}
.faq-title{left:133px;top:4000px;font-size:40px;font-weight:700;color:#222}
.faq-item{position:absolute;left:92px;width:1041px;border-bottom:1px solid #777;font-size:23px;color:#222;padding-left:16px}
.faq-item span{position:absolute;right:18px;top:10px;font-size:22px;color:#777}

.footer .brand{left:34px;top:4478px;font-size:13px;line-height:1.3}
.footer .brand small{display:block;color:var(--green);font-size:11px}
</style>
</head>
<body>

<header class="photo hero" role="img" aria-label="Mountain lake with pine covered slopes and a person sitting on a wooden dock"></header>
<div class="brand" style="left:62px;top:62px;width:220px;font-size:16px;line-height:1.25"><span class="dot"></span>Wellness, Purpose, and the Quiet Path</div>
<nav class="nav">
  <a class="active" href="#">HOME</a><a href="#">PEOPLE</a><a href="#">PROJECTS</a><a href="#">FAQ</a><a href="#">RESOURCES</a><a href="#">CONTACT</a>
</nav>
<h1 class="hero-title">Health care delivery research</h1>
<p class="hero-sub">is conceptualized as the study<br>of cancer care, factors influencing care,<br>and outcomes of care.</p>

<div class="brand tag-brand"><span class="dot"></span><div>Wellness, Purpose, and the Quiet Path<small>The Research Program</small></div></div>
<h2 class="abs h-main intro-title">What is Lorem Ipsum?</h2>
<p class="abs intro-text">Lorem Ipsum is simply dummy text of the printing and typesetting industry. Lorem Ipsum has been the industry's standard dummy text ever since</p>

<section>
  <div class="card" style="left:92px">
    <div class="icon"><svg width="60" height="60" viewBox="0 0 60 60" fill="none" stroke="#1a5a97" stroke-width="3" stroke-linecap="round"><circle cx="30" cy="8" r="4"/><path d="M30 14v18h14l6 14"/><circle cx="26" cy="40" r="13" stroke="#2a8ad0"/></svg></div>
    <span class="label">Healthcare</span>
    <p>Lorem Ipsum is simply dummy text of the printing and typesetting industry. Lorem Ipsum has been the industry's standard dummy text ever since</p>
    <a class="btn btn-outline" href="#">Read More</a>
  </div>
  <div class="card" style="left:444px">
    <div class="icon"><svg width="60" height="64" viewBox="0 0 60 64" fill="none" stroke="#2a8ad0" stroke-width="8" stroke-linecap="round"><path d="M16 58L40 18a9 9 0 0 0-18 0l24 40"/></svg></div>
    <span class="label">Values</span>
    <p>Lorem Ipsum is simply dummy text of the printing and typesetting industry. Lorem Ipsum has been the industry's standard dummy text ever since</p>
    <a class="btn btn-outline" href="#">Read More</a>
  </div>
  <div class="card" style="left:802px">
    <div class="icon"><svg width="60" height="64" viewBox="0 0 60 64" fill="none" stroke="#1a5a97" stroke-width="4" stroke-linecap="round"><path d="M12 6v18a12 12 0 0 0 24 0V6"/><path d="M24 36v10a10 10 0 0 0 20 0V34"/><circle cx="44" cy="26" r="7" stroke="#2a8ad0"/></svg></div>
    <span class="label">Spiritual Life</span>
    <p>Lorem Ipsum is simply dummy text of the printing and typesetting industry. Lorem Ipsum has been the industry's standard dummy text ever since</p>
    <a class="btn btn-outline" href="#">Read More</a>
  </div>
</section>

<div class="photo doc-photo" role="img" aria-label="Doctor in a white coat talking with a patient at a desk"></div>
<h2 class="abs h-main about-title">What is Lorem Ipsum?</h2>
<p class="abs about-text">Lorem Ipsum is simply dummy text of the printing and typesetting industry. Lorem Ipsum has been the industry's standard dummy text ever since</p>
<a class="btn btn-solid about-btn" href="#">Read More</a>

<div class="photo spirit" role="img" aria-label="Woman meditating cross-legged on a beach by the water"></div>
<h2 class="abs h-main spirit-title">Spiritual Life</h2>
<div class="abs spirit-text">
  <p>Lorem Ipsum is simply dummy text of the printing and typesetting industry. Lorem Ipsum has been the industry's standard dummy text ever since</p>
  <p style="margin-top:41px;width:540px">Lorem Ipsum is simply dummy text of the printing and typesetting industry.</p>
</div>
<a class="btn btn-solid spirit-btn" href="#">Read More</a>

<h2 class="abs h-main people-title">People</h2>
<p class="abs people-text">Lorem Ipsum is simply dummy text of the printing and typesetting industry. Lorem Ipsum has been the industry's standard dummy text ever since</p>
<a class="btn btn-outline people-btn" href="#">Read More</a>

<div class="team" style="left:27px">
  <div class="head">Research Team</div>
  <div class="photo pic" style="position:relative;background:linear-gradient(135deg,#3b5f86,#d8c04a 70%,#e8e27a)" role="img" aria-label="Scientists in safety glasses examining test tubes"></div>
  <p>Lorem Ipsum is simply dummy text of the printing and typesetting industry. Lorem Ipsum has been</p>
  <a class="btn btn-outline" href="#">Read More</a>
</div>
<div class="team" style="left:419px">
  <div class="head">Advisory committee</div>
  <div class="photo pic" style="position:relative;background:linear-gradient(135deg,#eef0f2,#9aa3ad 55%,#2d3646)" role="img" aria-label="Group of professionals reviewing documents together"></div>
  <p>Lorem Ipsum is simply dummy text of the printing and typesetting industry. Lorem Ipsum has been</p>
  <a class="btn btn-solid" href="#">Read More</a>
</div>
<div class="team" style="left:807px">
  <div class="head">Partners</div>
  <div class="photo pic" style="position:relative;background:linear-gradient(135deg,#e9eaec,#b7b2ab 55%,#5a4d45)" role="img" aria-label="Colleagues shaking hands across a meeting table"></div>
  <p>Lorem Ipsum is simply dummy text of the printing and typesetting industry. Lorem Ipsum has been</p>
  <a class="btn btn-solid" href="#">Read More</a>
</div>

<div class="photo project" role="img" aria-label="Calculator and financial papers under a blue tint"></div>
<h2 class="abs project-title">Project</h2>
<p class="abs project-text">Lorem Ipsum is simply dummy text of the printing and typesetting industry. Lorem Ipsum has been the industry's standard dummy text ever since Lorem Ipsum is simply dummy text of the printing and typesetting industry. Lorem Ipsum has been the industry's standard dummy text ever since Lorem Ipsum is simply dummy text of the printing and typesetting industry. Lorem Ipsum has been the industry's standard dummy text ever since</p>
<a class="btn project-btn" href="#">Read More</a>

<div class="photo faq" role="img" aria-label="Faded hospital scene with a care worker and patient"></div>
<h2 class="abs faq-title">FAQ</h2>
<div class="faq-item" style="top:4090px;height:48px">What makes this project unique?<span>+</span></div>
<div class="faq-item" style="top:4160px;height:49px">Does this project assume that the impact of religion is always positive?<span>+</span></div>
<div class="faq-item" style="top:4230px;height:50px">How can I collaborate?<span>+</span></div>
<div class="faq-item" style="top:4309px;height:49px">Will Thornbury faculty lead all projects?<span>+</span></div>

<footer class="footer">
  <div class="brand"><span class="dot"></span><div>Wellness, Purpose, and the Quiet Path<small>The Research Program</small></div></div>
</footer>

</body>
</html>
```